Business card design needed

www.corvanfab.com.au
Our primary services:
On-site welding.
On-site industrial maintenance.
On-site repairs and capital works projects specialising in pipe fabrication.
Our ability to work on-site with our dedicated mobile equipment is essential to our capability to provide a quality maintenance service to our customers. We are capable of providing a full team of qualified boilermakers that can work either to your plan or project manage if a plan has not been developed.
Industry/Entity Type
Industrial
Contact Information for Business Card
company name- CORVAN FAB PTY LTD
story - industrial steel fabrication, constructions and pipelines
Director - Greg Halvey
workshop address - shed 7, 3820 mirren rd Halston
postal address - P.O BOX 268 HALSTON Q 4870
mobile - 0438596204
w/shop phone - 0740593827
fax - 0740593828
email - admin@corvanfab.com.au
web - www.corvanfab.com.au
Logo Text
CORVAN FAB pty ltd

```html
<!DOCTYPE html>
<html lang="en">
<head>
<meta charset="utf-8">
<title>Corvan Fab – Business Card</title>
<link href="https://fonts.googleapis.com/css2?family=Black+Ops+One&family=Tinos:wght@400;700&display=swap" rel="stylesheet">
<style>
  :root {
    --page-bg: #f4eeee;
    --card-red: #c4423f;
    --card-red-dark: #b13a37;
    --logo-blue: #4a55a8;
    --ink-light: #f3ece9;
    --ink-grey: #ded4d1;
  }
  * { margin: 0; padding: 0; box-sizing: border-box; }
  html, body { width: 1200px; height: 900px; overflow: hidden; }
  body {
    background: var(--page-bg);
    display: flex; align-items: center; justify-content: center;
    font-family: "Tinos", "Times New Roman", serif;
  }
  .business-card {
    position: relative;
    width: 840px; height: 480px;
    background: radial-gradient(ellipse at 40% 40%, var(--card-red), var(--card-red-dark));
    border-radius: 6px;
    box-shadow: 0 12px 30px rgba(0,0,0,.25);
    color: var(--ink-light);
  }
  .brand {
    position: absolute; left: 70px; top: 92px;
    display: flex; align-items: center; gap: 14px;
  }
  .brand-mark { width: 22px; height: 22px; background: var(--logo-blue); }
  .brand-name {
    font-size: 38px; font-weight: 400; color: var(--logo-blue); letter-spacing: 1px;
    white-space: nowrap;
  }
  .identity { position: absolute; left: 460px; top: 88px; }
  .person-name {
    font-family: "Black Ops One", "Impact", sans-serif;
    font-size: 40px; font-weight: 400; color: var(--ink-grey);
    letter-spacing: 1px; line-height: 1; white-space: nowrap;
  }
  .person-role {
    font-size: 32px; color: var(--ink-grey); letter-spacing: 2px;
    margin-left: 60px; line-height: 1.1;
  }
  .contact-details {
    position: absolute; left: 470px; top: 240px; font-size: 14px;
    white-space: nowrap;
  }
  .contact-line { display: flex; align-items: center; gap: 10px; margin-top: 8px; }
  .contact-line .icon { width: 36px; height: 24px; flex: none; }
  .contact-line .email-text { font-size: 17px; }
  .website { font-size: 24px; margin-top: 6px; letter-spacing: .5px; }
  .phone-list {
    position: absolute; left: 50px; top: 300px; list-style: none;
  }
  .phone-list li {
    display: flex; align-items: center; gap: 14px;
    font-size: 36px; letter-spacing: 1px; line-height: 1.2;
  }
  .phone-list .icon { width: 34px; height: 38px; flex: none; }
</style>
</head>
<body>
  <section class="business-card" role="img" aria-label="Red business card with a faint steel tread-plate texture">
    <div class="brand">
      <span class="brand-mark"></span>
      <span class="brand-name">CORVAN FAB</span>
    </div>

    <div class="identity">
      <h1 class="person-name">GREG HALVEY</h1>
      <p class="person-role">Director</p>
    </div>

    <div class="contact-details">
      <p class="address">Adress : shed 7, 3820 mirren rd Halston</p>
      <div class="contact-line">
        <svg class="icon" viewBox="0 0 36 24" fill="none" stroke="#f3ece9" stroke-width="1.6">
          <rect x="1" y="1" width="34" height="22"/>
          <rect x="26" y="4" width="6" height="6"/>
          <line x1="5" y1="14" x2="20" y2="14"/><line x1="5" y1="18" x2="20" y2="18"/>
        </svg>
        <span>P.O BOX 268 HALSTON Q 4870</span>
      </div>
      <div class="contact-line">
        <svg class="icon" viewBox="0 0 36 24" fill="none" stroke="#f3ece9" stroke-width="1.6">
          <rect x="1" y="1" width="34" height="22"/>
          <polyline points="1,1 18,14 35,1"/>
        </svg>
        <span class="email-text">admin@corvanfab.com.au</span>
      </div>
      <p class="website">www.corvanfab.com.au</p>
    </div>

    <ul class="phone-list">
      <li>
        <svg class="icon" viewBox="0 0 34 38" fill="none" stroke="#f3ece9" stroke-width="2">
          <rect x="8" y="2" width="18" height="34" rx="3"/>
          <line x1="14" y1="31" x2="20" y2="31"/>
        </svg>
        <span>0438596204</span>
      </li>
      <li>
        <svg class="icon" viewBox="0 0 34 38" fill="#f3ece9">
          <path d="M8 4c3-2 5 0 6 3l1 4c0 2-2 3-3 4 1 4 4 8 8 10 1-1 2-3 4-3l4 1c3 1 4 4 2 6-3 4-8 4-13 0C9 25 5 18 5 11c0-3 1-5 3-7z"/>
        </svg>
        <span>0740593827</span>
      </li>
      <li>
        <svg class="icon" viewBox="0 0 34 38" fill="none" stroke="#f3ece9" stroke-width="2">
          <rect x="9" y="3" width="16" height="10"/>
          <rect x="3" y="13" width="28" height="14" rx="2"/>
          <rect x="9" y="24" width="16" height="11" fill="#f3ece9"/>
        </svg>
        <span>0740593828</span>
      </li>
    </ul>
  </section>
</body>
</html>
```